Stationery For Upscale Concierge Company

Create stationary that looks good in black and white and uses the attached logo. Needs to be upscale using upscale fonts and layout. Use the attached logo. Reverse out if necessary.

```html
<!DOCTYPE html>
<html lang="en">
<head>
<meta charset="UTF-8">
<title>Meridian Bridge — Business Cards</title>
<link href="https://fonts.googleapis.com/css2?family=Montserrat:wght@700&family=Open+Sans:wght@400&display=swap" rel="stylesheet">
<style>
  :root {
    --backdrop: #8c8c8c;
    --card: #0d0d0d;
    --ink: #ffffff;
    --ink-soft: #bdbdbd;
    --ink-muted: #8a8a8a;
    --rule: #5a5a5a;
  }
  * { margin: 0; padding: 0; box-sizing: border-box; }
  html, body { width: 1200px; height: 1200px; overflow: hidden; }
  body {
    background: var(--backdrop);
    font-family: "Open Sans", sans-serif;
    position: relative;
  }
  .card {
    position: absolute;
    left: 250px;
    width: 700px;
    height: 400px;
    background: var(--card);
    color: var(--ink);
    box-shadow: 0 10px 30px rgba(0,0,0,0.35);
  }
  .card--front { top: 120px; }
  .card--back { top: 610px; }

  .brand {
    display: flex;
    align-items: center;
    gap: 14px;
    font-family: "Open Sans", sans-serif;
    font-weight: 400;
    text-transform: uppercase;
    letter-spacing: 0.14em;
    color: var(--ink);
  }
  .brand__mark {
    width: 12px;
    height: 12px;
    background: var(--ink);
  }
  .card--front .brand {
    position: absolute;
    left: 0; right: 0; top: 0; bottom: 0;
    justify-content: center;
    font-size: 36px;
  }
  .card--back .brand {
    position: absolute;
    right: 80px;
    top: 60px;
    font-size: 26px;
  }

  .divider {
    position: absolute;
    left: 280px;
    right: 40px;
    top: 170px;
    height: 1px;
    background: var(--rule);
  }
  .address {
    position: absolute;
    right: 40px;
    top: 186px;
    text-align: right;
    font-size: 14px;
    line-height: 1.45;
    color: var(--ink-muted);
  }

  .person {
    position: absolute;
    left: 40px;
    top: 240px;
    width: 260px;
  }
  .person__name {
    font-family: "Montserrat", sans-serif;
    font-weight: 700;
    font-size: 19px;
    letter-spacing: 0.01em;
  }
  .person__title {
    font-size: 14px;
    color: var(--ink-soft);
    margin-top: 2px;
  }
  .person__rule {
    height: 1px;
    background: var(--rule);
    margin: 12px 0 12px;
  }
  .contact-list { list-style: none; }
  .contact-list li {
    display: flex;
    align-items: center;
    gap: 10px;
    font-size: 14px;
    line-height: 1.5;
    color: var(--ink);
  }
  .contact-list svg { width: 12px; height: 12px; fill: var(--ink); flex: none; }
</style>
</head>
<body>

<section class="card card--front" aria-label="Card front">
  <div class="brand"><span class="brand__mark"></span>Meridian Bridge</div>
</section>

<section class="card card--back" aria-label="Card back">
  <div class="brand"><span class="brand__mark"></span>Meridian Bridge</div>
  <div class="divider"></div>
  <address class="address" style="font-style:normal">
    Rear 18 – 22 Alder Lane<br>
    Westbrook NSW 2150
  </address>

  <div class="person">
    <div class="person__name">DANIEL HART</div>
    <div class="person__title">President</div>
    <div class="person__rule"></div>
    <ul class="contact-list">
      <li>
        <svg viewBox="0 0 24 24" aria-hidden="true"><path d="M6.6 10.8a15.1 15.1 0 0 0 6.6 6.6l2.2-2.2c.3-.3.7-.4 1-.2 1.1.4 2.3.6 3.6.6.6 0 1 .4 1 1V20c0 .6-.4 1-1 1C10.6 21 3 13.4 3 4c0-.6.4-1 1-1h3.5c.6 0 1 .4 1 1 0 1.3.2 2.5.6 3.6.1.3 0 .7-.2 1l-2.3 2.2z"/></svg>
        (555) 014-2290
      </li>
      <li>
        <svg viewBox="0 0 24 24" aria-hidden="true"><path d="M2 5h20v14H2z M2 5l10 8 10-8" /></svg>
        hello@meridianbridge.com
      </li>
      <li>
        <svg viewBox="0 0 24 24" aria-hidden="true"><path d="M12 2a10 10 0 1 0 0 20 10 10 0 0 0 0-20zm0 2c1.2 1.5 2 3.6 2.2 7H9.8C10 7.6 10.8 5.5 12 4zm-2.2 9h4.4c-.2 3.4-1 5.5-2.2 7-1.2-1.5-2-3.6-2.2-7z"/></svg>
        www.meridianbridge.com
      </li>
    </ul>
  </div>
</section>

</body>
</html>
```